Outdoor Billboard on PVC (double sides)

Hello, i need special design for billboard which is located 15 meters away from the main road. Measures form Billboard: 8 meters X 2 meters. I need Billboard for Window tinting. I have one picture (white Brevanti) which you can use as a main BIG Picture- or you have better idea i am so open to your suggestions. Billboard has to be shocking ... i want to make it look like this is similiar way from style. I have a lot of pictures from my cars which i have done in my garage which we can use it. I dont know if you can use this ... quality? On the billboard so it blames be turn left in 30Meter. My logo wants bi attached- please use it on black background. text which schould be down on the Billboard: Proffesionale Tint my logo VELUNAR put somewhere where looks cool Phone: 0681 2495 307 E-mail: marlow.velunar@kestramail.com Website: www. velunar-glasdunkel.at

Target Market(s)

This billboard wants to be on the border between two countrys..i have my garage company here on the border- where ia am making window. A lot of cars are driving each day nearby so I want that people see this and so they look at where they have left to my garage.

Colors

Designer to choose colors to be used in the design.

Requirements
Must have
• Billboard schould have a BiG picture from white Brevanti with my logo on the side and text Proffesional scarf tint. Down on the board it schould be info Tel, email, website. This measures 8x2 meters

```html
<!DOCTYPE html>
<html lang="de">
<head>
<meta charset="utf-8">
<title>VELUNAR – Billboard Scheibentönung</title>
<link rel="stylesheet" href="https://fonts.googleapis.com/css2?family=Kanit:ital,wght@1,900&family=Michroma&display=swap">
<style>
  :root {
    --stage: #d6d6d6;
    --board-black: #0d0d0e;
    --red: #e0060f;
    --red-deep: #9c0309;
    --silver-light: #ffffff;
    --silver-mid: #c9cbcf;
    --silver-dark: #7d8087;
    --white: #ffffff;
    --stripe-grey: #b8b8b8;
  }
  * { margin: 0; padding: 0; box-sizing: border-box; }
  html, body {
    width: 1200px; height: 349px; overflow: hidden;
    background: var(--stage);
  }
  .billboard {
    position: absolute; left: 32px; top: 32px;
    width: 1136px; height: 284px;
    background: var(--board-black);
    overflow: hidden;
  }
  .billboard__shapes { position: absolute; inset: 0; }
  .headline {
    position: absolute; left: 46px; top: 30px;
    font-family: "Kanit", sans-serif; font-style: italic; font-weight: 900;
    font-size: 54px; line-height: 54px; letter-spacing: 0.5px;
    text-transform: uppercase;
    transform: rotate(-5deg); transform-origin: left top;
  }
  .headline__line {
    display: block;
    background: linear-gradient(180deg, var(--silver-light) 0%, var(--silver-mid) 50%, var(--silver-dark) 100%);
    -webkit-background-clip: text; background-clip: text; color: transparent;
    filter: drop-shadow(3px 2px 0 var(--red));
  }
  .headline__line--second { padding-left: 6px; }
  .contact-list {
    position: absolute; left: 46px; top: 196px;
    list-style: none;
    transform: rotate(-5deg); transform-origin: left top;
  }
  .contact-list__item {
    display: flex; align-items: center; gap: 10px;
    height: 24px;
    font-family: "Michroma", sans-serif; font-size: 14px;
    color: var(--white); text-transform: uppercase; white-space: nowrap;
  }
  .contact-list__icon { width: 15px; height: 15px; flex: none; }
  .brand-mark {
    position: absolute; right: 28px; top: 84px;
    display: flex; align-items: center; gap: 8px;
  }
  .brand-mark__dot {
    width: 14px; height: 14px; border-radius: 50%;
    background: var(--red);
  }
  .brand-mark__name {
    font-family: "Michroma", sans-serif; font-size: 19px;
    color: var(--red);
  }
</style>
</head>
<body>
  <section class="billboard" aria-label="Billboard VELUNAR Scheibentönung">
    <svg class="billboard__shapes" width="1136" height="284" viewBox="0 0 1136 284">
      <defs>
        <linearGradient id="red-band" x1="0" y1="0" x2="1" y2="1">
          <stop offset="0" stop-color="#e0060f"/>
          <stop offset="1" stop-color="#9c0309"/>
        </linearGradient>
        <radialGradient id="car-photo" cx="0.58" cy="0.6" r="0.5"
                        gradientTransform="translate(0.58 0.6) scale(1 0.55) translate(-0.58 -0.6)">
          <stop offset="0" stop-color="#f5f7fb"/>
          <stop offset="0.55" stop-color="#dde2ea"/>
          <stop offset="0.78" stop-color="#6c717a"/>
          <stop offset="1" stop-color="#0c0c0e"/>
        </radialGradient>
        <linearGradient id="left-shade" x1="0" y1="0" x2="1" y2="0">
          <stop offset="0" stop-color="#0d0d0e"/>
          <stop offset="0.7" stop-color="#1e1e21"/>
          <stop offset="1" stop-color="#141416"/>
        </linearGradient>
      </defs>
      <rect class="backdrop" x="0" y="0" width="700" height="284" fill="url(#left-shade)"/>
      <polygon class="photo-area" role="img" aria-label="Foto: weißer Brevanti Sportwagen in Seitenansicht in einer dunklen Garage"
               points="680,0 1136,0 1136,284 560,284" fill="url(#car-photo)"/>
      <polygon class="band band--top" points="0,0 320,0 0,36" fill="#e0060f"/>
      <polygon class="band band--bottom" points="0,188 656,124 566,284 0,284" fill="url(#red-band)"/>
      <polygon class="stripe stripe--red" points="672,0 702,0 597,284 567,284" fill="#e0060f"/>
      <polygon class="stripe stripe--grey" points="710,0 722,0 620,284 608,284" fill="#b8b8b8"/>
      <polygon class="stripe stripe--floor" points="610,284 1136,252 1136,264 650,284" fill="#e0060f"/>
    </svg>

    <h1 class="headline">
      <span class="headline__line">Proffesionelle</span>
      <span class="headline__line headline__line--second">Scheibentönung</span>
    </h1>

    <ul class="contact-list">
      <li class="contact-list__item">
        <svg class="contact-list__icon" viewBox="0 0 16 16" aria-hidden="true">
          <circle cx="8" cy="8" r="7" fill="none" stroke="#fff" stroke-width="1.3"/>
          <path d="M5.5 4.5 l1.5 0 l0.6 2 l-1 0.8 a5 5 0 0 0 2.1 2.1 l0.8 -1 l2 0.6 l0 1.5 a1 1 0 0 1 -1 1 a6 6 0 0 1 -6 -6 a1 1 0 0 1 1 -1z" fill="#fff"/>
        </svg>
        0681 2495 307
      </li>
      <li class="contact-list__item">
        <svg class="contact-list__icon" viewBox="0 0 16 16" aria-hidden="true">
          <rect x="1.5" y="3.5" width="13" height="9" fill="none" stroke="#fff" stroke-width="1.3"/>
          <path d="M1.5 3.5 L8 9 L14.5 3.5" fill="none" stroke="#fff" stroke-width="1.3"/>
        </svg>
        marlow.velunar@kestramail.com
      </li>
      <li class="contact-list__item">
        <svg class="contact-list__icon" viewBox="0 0 16 16" aria-hidden="true">
          <circle cx="8" cy="8" r="6.5" fill="none" stroke="#fff" stroke-width="1.3"/>
          <ellipse cx="8" cy="8" rx="3" ry="6.5" fill="none" stroke="#fff" stroke-width="1.1"/>
          <line x1="1.5" y1="8" x2="14.5" y2="8" stroke="#fff" stroke-width="1.1"/>
        </svg>
        www.velunar-glasdunkel.at
      </li>
    </ul>

    <div class="brand-mark">
      <span class="brand-mark__dot"></span>
      <span class="brand-mark__name">VELUNAR</span>
    </div>
  </section>
</body>
</html>
```